7th Annual Falcon Ridge Classic Flyer

Looking to design an updated eye catching flyer maybe with someone movement, sound, and color. Below is an attachment of the flyer I have used in the past. I need to add color, sound, and movement to the flyer. This is an advertisement for youth folk style wrestling. You may contact me directly at 252-381-4927 if you need additional information. I really like the colors music and movement in the video below.
https://www.vidloomer.com/watch?v=kQ7mTbLw2Ra

Target Market(s)

Youth Wrestling

Font styles to use
Serif

Colors
EB3D1F
EC4F4E
F09395
F8D3D4
FCEDEE

Requirements
Must have
• All information included on flyer.
Nice to have
• Color, sound, and movement

```html
<!DOCTYPE html>
<html lang="en">
<head>
<meta charset="utf-8">
<title>7th Annual Falcon Ridge Classic</title>
<link rel="stylesheet" href="https://fonts.googleapis.com/css2?family=Alfa+Slab+One&family=Oswald:wght@500;600&display=swap">
<style>
:root{
  --flame:#EB3D1F;
  --coral:#EC4F4E;
  --rose:#F09395;
  --blush:#F8D3D4;
  --petal:#FCEDEE;
  --page:#ffffff;
  --cream:#f6ece0;
  --sand:#d9b894;
  --tan:#a9774a;
  --brown:#8a5a32;
  --panel:rgba(120,76,38,.84);
  --maroon:#6e1218;
  --maroon-dark:#3d0a0e;
  --gold:#e8a03a;
  --gold-dark:#8c5213;
  --ribbon:#b8823e;
  --ink:#141010;
  --white:#ffffff;
}
*{box-sizing:border-box;margin:0;padding:0}
html,body{width:811px;height:1200px;overflow:hidden;background:var(--page)}
body{position:relative;font-family:"Oswald",sans-serif}
.flyer{
  position:absolute;left:25px;top:23px;width:761px;height:1081px;overflow:hidden;
  background:linear-gradient(180deg,var(--cream) 0%,#efdcc4 22%,var(--sand) 50%,var(--tan) 78%,var(--brown) 100%);
  box-shadow:0 2px 8px rgba(0,0,0,.35);
}
.title{
  position:absolute;left:24px;top:26px;width:560px;text-align:center;
  font-family:"Alfa Slab One",serif;font-weight:400;text-transform:uppercase;color:var(--gold);
  line-height:1;white-space:nowrap;
  text-shadow:2px 2px 0 var(--gold-dark),3px 3px 0 #3a2414,4px 5px 6px rgba(0,0,0,.4);
}
.title .line1{display:block;font-size:31px}
.title .line2{display:block;font-size:62px;margin-top:8px}
.badge{
  position:absolute;left:611px;top:0;width:151px;height:166px;
  background:var(--ribbon);
  clip-path:polygon(0 0,100% 0,100% 100%,50% 86%,0 100%);
  text-align:center;color:var(--ink);padding-top:24px;
}
.badge .badge-name{font-family:"Alfa Slab One",serif;font-size:14px;letter-spacing:1px}
.badge .badge-dot{display:block;width:40px;height:40px;border-radius:50%;border:2px solid var(--ink);margin:8px auto}
.badge .badge-sub{font-family:"Alfa Slab One",serif;font-size:7px;line-height:1.25;padding:0 14px;text-transform:uppercase}
.event-date{
  position:absolute;left:74px;top:172px;font-family:"Oswald",sans-serif;font-weight:600;
  font-size:30px;line-height:36px;color:var(--ink);text-transform:uppercase;letter-spacing:.3px;
}
.schedule-band{
  position:absolute;left:0;top:221px;width:761px;height:96px;
  background:linear-gradient(90deg,var(--maroon) 0%,var(--maroon) 60%,var(--maroon-dark) 100%);
  color:var(--petal);text-align:center;padding-top:11px;padding-right:250px;
  font-weight:600;font-size:16.5px;line-height:27px;text-transform:uppercase;
}
.schedule-band p{white-space:nowrap}
.details{
  position:absolute;left:0;top:827px;width:761px;height:254px;
  background:linear-gradient(180deg,rgba(150,98,52,.55),rgba(130,84,42,.75));
}
.hero-figure{
  position:absolute;left:505px;top:240px;width:256px;height:841px;
  background:radial-gradient(ellipse at 60% 22%,#9a2a22 0%,#5a2a1c 40%,#2e1c13 75%,#2a1a12 100%);
  border-radius:48% 0 0 0;
}
.panel{
  position:absolute;left:0;width:498px;background:var(--panel);
  border-radius:0 12px 12px 0;color:var(--white);text-align:center;text-transform:uppercase;
  padding-right:28px;
}
.fees{top:323px;height:134px;padding-top:12px;font-size:12.5px;line-height:21.5px;font-weight:500}
.pill{
  position:absolute;height:33px;background:linear-gradient(90deg,var(--maroon) 0%,#2a0608 100%);
  border-radius:8px;color:var(--petal);font-family:"Alfa Slab One",serif;font-weight:400;text-transform:uppercase;
  font-size:18px;line-height:33px;text-align:center;white-space:nowrap;z-index:2;
}
.boys-heading{left:134px;top:466px;width:226px}
.girls-heading{left:134px;top:640px;width:226px}
.weighin-heading{left:164px;top:801px;width:168px}
.boys{top:491px;height:142px;padding-top:17px;font-size:10.5px;line-height:16.8px;font-weight:500}
.girls{top:666px;height:85px;padding-top:15px;font-size:10.5px;line-height:16.8px;font-weight:500;padding-left:34px;padding-right:56px}
.notes{
  position:absolute;left:0;top:757px;width:470px;text-align:center;color:var(--ink);
  font-size:10px;line-height:17px;font-weight:600;text-transform:uppercase;
}
.details-text{
  position:absolute;left:30px;top:840px;width:460px;color:var(--white);text-transform:uppercase;
  font-size:9px;line-height:15.4px;font-weight:500;
}
.details-text p{white-space:nowrap}
.details-text .gap{height:14px}
.details-text .indent{padding-left:10px}
</style>
</head>
<body>
<main class="flyer">
  <h1 class="title"><span class="line1">7th Annual Falcon Ridge</span><span class="line2">Classic</span></h1>

  <div class="badge">
    <div class="badge-name">CYGL</div>
    <span class="badge-dot"></span>
    <div class="badge-sub">Carolina's Premier Youth Grappling League</div>
  </div>

  <h2 class="event-date">Saturday, January 25, 2025</h2>

  <div class="details"></div>
  <div class="hero-figure" role="img" aria-label="Armoured warrior in a crested helmet and red cloak holding a spear"></div>

  <section class="schedule-band">
    <p>4U, 6U, 8U, 10U — Wrestling Starts at 8:30 AM</p>
    <p>12U, Middle School, &amp; High School — Wrestling Starts at 1:00 PM</p>
    <p>Register @ www.matentryhub.com</p>
  </section>

  <section class="panel fees">
    <p>Early Registration $30.00 Deadline is January 19, 2025 at 11:59PM</p>
    <p>Regular Registration $40.00 Deadline is January 22, 2025 at 11:59PM</p>
    <p>Late Registration $50.00 Deadline is January 24, 2025 at 5:00PM</p>
    <p>Registration is limited to the first 500 wrestlers</p>
    <p>Non-CYGL Card Holders will pay an additional $5.00 at weigh-ins.</p>
  </section>

  <h3 class="pill boys-heading">Boys Divisions:</h3>
  <section class="panel boys">
    <p>4 &amp; Under - 30, 40, 50, HWT</p>
    <p>6 &amp; Under - 36, 40, 44, 48, 52, 56, 60, HWT</p>
    <p>8 &amp; Under - 40, 44, 48, 52, 56, 60, 64, 68, 72, 76, 80, 84, 88, 92, HWT</p>
    <p>10 &amp; Under - 52, 56, 60, 64, 68, 72, 76, 80, 84, 88, 92, 96, 100, 110, HWT</p>
    <p>12 &amp; Under - 64, 68, 72, 76, 80, 84, 88, 92, 96, 100, 105, 110, 115, 120, 130, 140, 160, HWT</p>
    <p>Middle School - 72, 76, 80, 88, 92, 96, 100, 105, 110, 115, 120, 130, 140, 160, 210, HWT</p>
    <p>High School - 106, 113, 120, 126, 132, 138, 144, 150, 157, 165, 175, 190, 215, HWT</p>
  </section>

  <h3 class="pill girls-heading">Girls Divisions:</h3>
  <section class="panel girls">
    <p>K-5 - 36, 40, 44, 48, 52, 56, 60, 64, 68, 72, 76, 80, 84, 88, 92, 96, 100, 110, 120, HWT</p>
    <p>Middle School — 72, 76, 83, 90, 98, 106, 113, 120, 126, 132, 138, 145, 152, 160, 170, 182, 190, 220, HWT</p>
    <p>Women's High School 100, 107, 114, 120, 126, 132, 145, 152, 165, 185, HWT</p>
  </section>

  <div class="notes">
    <p>*Age is based upon wrestler's age as of December 31, 2024.</p>
    <p>Tournament director has the right to combine weight classes if deemed necessary.</p>
  </div>

  <h3 class="pill weighin-heading">Weigh-ins:</h3>
  <section class="details-text">
    <p>January 24, 2025 – 5:00 PM to 7:00 PM (Early Weigh-ins - $10 cash due at scale)</p>
    <p>January 25, 2025 – 6:00 AM to 7:30 AM (4U, 6U, 8U, 10U)</p>
    <p>January 25, 2025 – 11:00 AM to 12:00 PM (12 &amp; Under, MS, &amp; High School)</p>
    <div class="gap"></div>
    <div class="indent">
      <p>Tenths are waived/dropped at weigh-ins. Satellite weigh-ins will not be allowed.</p>
      <p>High School Divisions are given 2 lbs. growth allowance.</p>
      <p>Custom medals will be given to the top 3 individual finishers in each bracket.</p>
    </div>
    <div class="gap"></div>
    <p>Custom Awards will be awarded to the top 4 teams. Referee decisions will be final.</p>
    <p>Pine Hollow Athletics is not responsible for accidents, injuries, or theft during the tournament.</p>
    <p>Admission: $10.00 per person</p>
    <p>For more information, contact Tournament Director Dale Whitford: (252) 381-4927</p>
    <p>Hotels Available On-Site</p>
    <p>Riverside Lodge (252) 417-2260 / Oakline Suites (252) 417-3380 / Harbor Crest Inn (252) 417-5140</p>
  </section>
</main>
</body>
</html>
```